Business card for a gourmet fruit and vegetable retail store

Please design a business card for our boutique gourmet fruit and vegetable food store using attached logo design, with the colour options of white, black and lime green. We would like it to be unique and classic, with a large image of the logo on the back of the business card, and the business card details plus a design on the front.

Target Market(s)

High income earners in an affluent Melbourne suburb who value high quality products and done mind paying for it

Industry/Entity Type

Retail

Contact Information for Business Card

Business name: Harwick's Fine Food Merchant
Address: 27 Plumtree Rd, Kelsby VIC 3158
Name: TBC
Position Title: Director
Phone Number: TBC
Mobile: TBC

Business name is: Harwick's Fine Food Merchant. Please allow space for us to fill in the business address, contact number, person's name, position Title and mobile number.

Colors
acd036

Requirements
Must have
• The logo must have our business logo on the back, and our business details and contact details on the front. It must include the colours of white, black and lime green
Nice to have
• It can have different background colours on the front and on the back.
Should not have
• It should not have any other colours aside from white, black and lime green

```html
<!DOCTYPE html>
<html lang="en">
<head>
<meta charset="utf-8">
<title>Harwick's Fine Food Merchant – Business Card</title>
<link href="https://fonts.googleapis.com/css2?family=Arvo:wght@400;700&display=swap" rel="stylesheet">
<style>
  :root {
    --backdrop: #1c1c1c;
    --card: #0e0e0e;
    --card-edge: #1a1a1a;
    --lime: #acd036;
    --white: #ffffff;
    --rule: #d4d4d4;
  }
  * { box-sizing: border-box; margin: 0; padding: 0; }
  html, body {
    width: 1200px;
    height: 873px;
    overflow: hidden;
    background: var(--backdrop);
    font-family: "Arvo", serif;
  }
  .canvas {
    position: relative;
    width: 1200px;
    height: 873px;
    display: flex;
    align-items: center;
    justify-content: center;
    gap: 40px;
  }
  .card {
    position: relative;
    width: 540px;
    height: 309px;
    border-radius: 16px;
    background: linear-gradient(135deg, var(--card-edge), var(--card));
    overflow: hidden;
  }

  /* Brand seal: name inside one plain circle */
  .seal {
    position: absolute;
    display: flex;
    align-items: center;
    justify-content: center;
    border-radius: 50%;
    border: 2px solid currentColor;
  }
  .seal__name {
    font-weight: 400;
    text-transform: uppercase;
    white-space: nowrap;
  }

  /* Back of card */
  .seal--back {
    left: 135px;
    top: 19px;
    width: 270px;
    height: 270px;
    color: var(--lime);
  }
  .seal--back .seal__name {
    font-size: 34px;
    letter-spacing: 3px;
  }

  /* Front of card */
  .card--front::after {
    content: "";
    position: absolute;
    left: 0; right: 0; bottom: 0;
    height: 8px;
    background: var(--lime);
  }
  .seal--front {
    right: 26px;
    top: 26px;
    width: 220px;
    height: 220px;
    color: var(--white);
  }
  .seal--front .seal__name {
    font-size: 26px;
    letter-spacing: 2.5px;
  }
  .person {
    position: absolute;
    left: 30px;
    top: 104px;
  }
  .person__name {
    color: var(--white);
    font-size: 24px;
    font-weight: 400;
    letter-spacing: 1.5px;
    line-height: 30px;
    text-transform: uppercase;
  }
  .person__title {
    color: var(--lime);
    font-size: 14px;
    font-weight: 700;
    letter-spacing: 1px;
    margin-top: 8px;
    text-transform: uppercase;
  }
  .person__rule {
    position: absolute;
    left: 30px;
    top: 138px;
    width: 264px;
    height: 1px;
    background: var(--rule);
  }
  .address {
    position: absolute;
    left: 30px;
    top: 172px;
    color: var(--white);
    font-size: 15px;
    line-height: 24px;
    font-style: normal;
    font-weight: 700;
  }
  .contact {
    position: absolute;
    left: 30px;
    bottom: 28px;
    list-style: none;
    color: var(--white);
    font-size: 16px;
    letter-spacing: 0.5px;
  }
  .contact__item {
    display: flex;
    align-items: center;
    gap: 10px;
    line-height: 25px;
  }
  .contact__icon {
    width: 15px;
    height: 15px;
    fill: var(--lime);
    flex: none;
  }
</style>
</head>
<body>
<main class="canvas">

  <section class="card card--back" aria-label="Card back">
    <div class="seal seal--back">
      <p class="seal__name">Harwick's</p>
    </div>
  </section>

  <section class="card card--front" aria-label="Card front">
    <div class="person">
      <h1 class="person__name">Daniel Reeve</h1>
      <p class="person__title">Director</p>
    </div>
    <div class="person__rule"></div>

    <address class="address">
      27 Plumtree Rd<br>
      Kelsby VIC 3158
    </address>

    <ul class="contact">
      <li class="contact__item">
        <svg class="contact__icon" viewBox="0 0 16 16" aria-hidden="true">
          <path d="M2 5c0-2 2-3 6-3s6 1 6 3v1h-3V4.5H5V6H2z"/>
          <rect x="3" y="7" width="10" height="7" rx="1.5"/>
        </svg>
        <span>0231-5578-4402</span>
      </li>
      <li class="contact__item">
        <svg class="contact__icon" viewBox="0 0 16 16" aria-hidden="true">
          <path d="M4.5 1h7a1 1 0 0 1 1 1v12a1 1 0 0 1-1 1h-7a1 1 0 0 1-1-1V2a1 1 0 0 1 1-1zm.5 2v9h6V3z"/>
        </svg>
        <span>0231-5578-4402</span>
      </li>
    </ul>

    <div class="seal seal--front">
      <p class="seal__name">Harwick's</p>
    </div>
  </section>

</main>
</body>
</html>
```